I need new business cards designed

I would like to get some new designs on business cards. I will upload my logo for reference. The business cards that were designed for me a few months ago were too difficult for the print companies to work with. My company is Brushwillow.net LLC. It is an art company that sells painting and expression cards online.

```html
<!DOCTYPE html>
<html lang="en">
<head>
<meta charset="utf-8">
<title>Brushwillow.net — Business Card</title>
<link rel="stylesheet" href="https://fonts.googleapis.com/css2?family=Open+Sans:wght@400;600;700&display=swap">
<style>
  :root {
    --backdrop: #1d1d1f;
    --card: #141414;
    --accent-blue: #1ba1dd;
    --text-light: #f2f2f2;
    --brand-indigo: #3d3f8f;
    --tagline: #d98a55;
    --emboss: #242424;
  }
  * { box-sizing: border-box; margin: 0; padding: 0; }
  html, body {
    width: 1200px; height: 900px; overflow: hidden;
    background: radial-gradient(ellipse at 50% 30%, #2c2c2e 0%, var(--backdrop) 70%);
    font-family: "Open Sans", Arial, sans-serif;
  }
  .sheet { position: relative; width: 1200px; height: 900px; }
  .card {
    position: absolute; left: 340px; width: 520px; height: 300px;
    background: var(--card); border-radius: 22px;
    box-shadow: 0 18px 40px rgba(0,0,0,.55);
  }
  .card--front { top: 100px; }
  .card--back { top: 480px; box-shadow: 0 6px 0 var(--accent-blue), 0 24px 40px rgba(0,0,0,.55); }

  /* front */
  .brand-lockup { position: absolute; left: 38px; top: 160px; display: flex; align-items: center; gap: 10px; }
  .brand-square { width: 40px; height: 40px; background: var(--accent-blue); flex: none; }
  .brand-name { font-size: 19px; font-weight: 400; color: var(--brand-indigo); line-height: 1.1; }
  .brand-tagline { font-size: 10.5px; color: var(--tagline); margin-top: 2px; white-space: nowrap; }
  .divider { position: absolute; left: 250px; top: 58px; width: 2px; height: 190px; background: var(--accent-blue); }
  .contact { position: absolute; left: 270px; top: 56px; color: var(--text-light); }
  .contact__name { font-size: 20px; font-weight: 700; color: var(--accent-blue); letter-spacing: .5px; }
  .contact__role { font-size: 12.5px; margin-bottom: 10px; }
  .contact__address { font-size: 12.5px; line-height: 1.45; margin-bottom: 10px; }
  .contact__line { display: flex; align-items: center; gap: 8px; font-size: 12.5px; line-height: 1.6; }
  .contact__line svg { width: 12px; height: 12px; fill: var(--accent-blue); flex: none; }
  .social { position: absolute; right: 34px; bottom: 34px; display: flex; gap: 8px; }
  .social span { width: 14px; height: 14px; border-radius: 50%; background: var(--accent-blue); }

  /* back */
  .emblem { position: absolute; left: 40px; top: 70px; width: 160px; height: 160px; background: var(--accent-blue); }
  .emboss { position: absolute; right: 36px; top: 122px; text-align: right; color: var(--emboss); }
  .emboss__name { font-size: 30px; font-weight: 400; line-height: 1.2; }
  .emboss__tagline { font-size: 13px; font-weight: 400; }
</style>
</head>
<body>
<main class="sheet">
  <section class="card card--front">
    <div class="brand-lockup">
      <div class="brand-square"></div>
      <div>
        <div class="brand-name">Brushwillow.net</div>
        <div class="brand-tagline">Paint Boldly · Share Freely</div>
      </div>
    </div>
    <div class="divider"></div>
    <div class="contact">
      <div class="contact__name">OWEN HARTLEY</div>
      <div class="contact__role">Managing Director</div>
      <div class="contact__address">Your address, City<br>State, Zip 1234</div>
      <div class="contact__line">
        <svg viewBox="0 0 24 24"><path d="M6.6 10.8a15 15 0 0 0 6.6 6.6l2.2-2.2a1 1 0 0 1 1-.25 11.4 11.4 0 0 0 3.6.57 1 1 0 0 1 1 1V20a1 1 0 0 1-1 1A17 17 0 0 1 3 4a1 1 0 0 1 1-1h3.5a1 1 0 0 1 1 1c0 1.25.2 2.45.57 3.6a1 1 0 0 1-.25 1z"/></svg>
        123-456-7890</div>
      <div class="contact__line">
        <svg viewBox="0 0 24 24"><path d="M2 5h20v14H2z M2 5l10 8 10-8" stroke="#141414" stroke-width="1.5"/></svg>
        info@brushwillow.net</div>
      <div class="contact__line">
        <svg viewBox="0 0 24 24"><circle cx="12" cy="12" r="10"/><path d="M2 12h20M12 2c3 3 3 17 0 20M12 2c-3 3-3 17 0 20" stroke="#141414" stroke-width="1.5" fill="none"/></svg>
        www.Brushwillow.net</div>
    </div>
    <div class="social" aria-label="Social media links"><span></span><span></span><span></span></div>
  </section>

  <section class="card card--back">
    <div class="emblem"></div>
    <div class="emboss">
      <div class="emboss__name">Brushwillow.net</div>
      <div class="emboss__tagline">Paint Boldly · Share Freely</div>
    </div>
  </section>
</main>
</body>
</html>
```